Silk Flower catalog for Cemeteries

We need a new catalog designed. I am looking for a cover page, a catalog content template page, and a back cover page.

We are Petals For Memorials and we supply silk flowers to cemeteries. We have a general color scheme on our website that I would like to stay close to. We are planning on printing them in house so I would not like to have a bleed. We will use 11x17 paper folded in half with staples down the center to form a standard booklet.

Cover Page / Front Cover - Simple large picture of a flower with the company name, not too fancy but elegant.

Catalog Page Templates - I want At least one (more possibly) pages which have areas that I can insert pictures. The pictures will have a model number and title associated with them in close proximity. The flower pictures should be the real star on the page. I would like a 3x3 grid for 9 pictures on the page. The flower pictures have a transparent background and are square.
There should also be a title area so that we can identify the product line that is contained on the page.

Back Cover - Standard back cover page with biographical information (address, phone., email, website...Ect.) Same as the front cover in that it needs to be elegant.

Many cemeteries do not have internet access and this will be used by cemeteries as a sales tool.

Our website is www.PetalsForMemorials.example
I have high resolution images of everything that I can use for the final product, low res images copies directly from the website may be used as placeholders to conceptualize the design.

I use Adobe inDesign frequently and would prefer this program be used for the final product so that I can add high res pictures and fill out the catalog.

We need a new catalog, it is highly unlikely this project will get refunded. If you have any questions please ask, I will answer asap.
Updates

I have a few designs that are heading in the right direction. I went ahead and committed the payment so that it is not refundable anymore.  I look forward to seeing your designs/revisions!

We have narrowed it down to one design and are waiting on one more change before closing the project.

Thank you for your submissions 

Target Market(s)

Cemetery sales people who sit down with a family who has recently lost a loved one.

Industry/Entity Type

Printing

Font styles to use
Serif
Sans Serif

Requirements
Must have
• Front Cover, One or more pages to be used a templates for content, back cover.

Color scheme must be close to the existing pallet that is used on the website listed. We have built our brand around these colors, however we will consider nice looking minor deviations.

Page background must be white.
No page bleed.
Nice to have
• Large, easy to read print for elderly people on the catalog template pages.
Font choice does not matter, however we have used georgia font frequently in the past.
I am very open to new ideas.

```html
<!DOCTYPE html>
<html lang="en">
<head>
<meta charset="utf-8">
<title>Petals For Memorials – Catalog Spread</title>
<link href="https://fonts.googleapis.com/css2?family=Open+Sans:wght@600;700&display=swap" rel="stylesheet">
<style>
  :root{
    --paper:#ffffff;
    --wash-green:#eef4e6;
    --wash-blue:#eef4f8;
    --title-red:#c33a2c;
    --code-grey:#3c3c3c;
    --label-top:#f1f1f1;
    --label-bottom:#dedede;
    --pill-top:#9fae9f;
    --pill-bottom:#6f806f;
    --rule:#b9c3b5;
    --trim:#7a7a7a;
    --band-grey:#a9b6a4;
    --band-red:#b5342c;
    --band-gold:#f0bc4a;
  }
  *{box-sizing:border-box;margin:0;padding:0}
  html,body{width:1200px;height:1000px;overflow:hidden;background:var(--paper)}
  body{position:relative;font-family:"Open Sans",Arial,sans-serif}

  .spread{position:absolute;left:30px;top:155px;width:1140px;height:740px;
    box-shadow:0 4px 14px rgba(0,0,0,.35);background:var(--paper);overflow:hidden}
  .spread-texture{position:absolute;inset:0;
    background:linear-gradient(90deg,var(--wash-green) 0%,#f7faf3 30%,#fbfcfa 50%,#f6f9f7 70%,var(--wash-blue) 100%)}

  .page{position:absolute;top:0;width:570px;height:740px}
  .page--left{left:0}
  .page--right{left:570px}

  .page-rule{position:absolute;left:0;right:0;top:34px;height:2px;background:var(--rule)}
  .section-title{position:absolute;top:22px;left:50%;transform:translateX(-50%);
    width:268px;height:29px;border-radius:15px;
    background:linear-gradient(var(--pill-top),var(--pill-bottom));
    color:#fff;font-weight:700;font-size:19px;line-height:29px;text-align:center;white-space:nowrap;
    box-shadow:0 1px 2px rgba(0,0,0,.3)}
  .flourish{position:absolute;top:24px;width:44px;height:24px;border-radius:12px;
    background:radial-gradient(#cfd4cf,rgba(207,212,207,0) 70%)}
  .flourish--left{left:calc(50% - 182px)}
  .flourish--right{left:calc(50% + 138px)}

  .product-grid{position:absolute;left:20px;top:67px;width:532px;
    display:grid;grid-template-columns:repeat(3,166px);column-gap:17px;
    grid-template-rows:208px 222px 216px}
  .product{display:flex;flex-direction:column;align-items:center}
  .product-photo{width:140px;height:140px;border-radius:4px;flex:none}
  .product-label{margin-top:6px;width:162px;height:52px;padding:3px 10px 4px;
    background:linear-gradient(var(--label-top),var(--label-bottom));
    box-shadow:0 2px 3px rgba(0,0,0,.18);text-align:center;
    display:flex;flex-direction:column;justify-content:center}
  .product:nth-child(n+4) .product-label{height:66px}
  .product-name{color:var(--title-red);font-weight:700;font-size:14px;line-height:16.5px}
  .product-code{color:var(--code-grey);font-weight:700;font-size:11.5px;line-height:15px;margin-top:3px}

  .tone-tree{background:radial-gradient(circle at 50% 55%,#2f5a2a,#6a8a4e 45%,#fff 72%)}
  .tone-poinsettia{background:radial-gradient(circle at 50% 40%,#e12b22,#b5201b 50%,#fff 75%)}
  .tone-amaryllis{background:radial-gradient(circle at 50% 45%,#a81b22,#4a6e3a 55%,#fff 76%)}
  .tone-mum{background:radial-gradient(circle at 50% 50%,#f2d84a,#5c86c9 45%,#3e6a34 60%,#fff 76%)}
  .tone-blue{background:radial-gradient(circle at 50% 50%,#3b62b8,#8db7e0 50%,#fff 75%)}
  .tone-poppy{background:radial-gradient(circle at 50% 45%,#d9481c,#e89a2a 50%,#fff 76%)}
  .tone-burgundy{background:radial-gradient(circle at 50% 50%,#6d1240,#c64a8a 45%,#3d6a34 60%,#fff 76%)}
  .tone-pink{background:radial-gradient(circle at 50% 50%,#f2a8c8,#f7d2e2 50%,#fff 76%)}
  .tone-yellow{background:radial-gradient(circle at 50% 50%,#f4d21c,#f6e45a 50%,#fff 76%)}

  .edge-band{position:absolute;left:0;right:0;bottom:0;height:10px;display:flex}
  .edge-band span{height:100%}
  .band-grey{background:var(--band-grey)}
  .band-red{background:var(--band-red)}
  .band-gold{background:var(--band-gold)}

  .trim{position:absolute;border:0 dashed var(--trim)}
  .trim--h{left:20px;width:1160px;border-top-width:1px}
  .trim--v{top:145px;height:760px;border-left-width:1px}
</style>
</head>
<body>
  <main class="spread">
    <div class="spread-texture" role="img" aria-label="Faint light green and blue line pattern background"></div>

    <section class="page page--left">
      <div class="page-rule"></div>
      <div class="flourish flourish--left" role="img" aria-label="Silver ornamental flourish"></div>
      <div class="flourish flourish--right" role="img" aria-label="Silver ornamental flourish"></div>
      <h2 class="section-title">Ground Vase (Large)</h2>
      <div class="product-grid">
        <article class="product"><div class="product-photo tone-tree" role="img" aria-label="Decorated Christmas tree arrangement with red bow"></div><div class="product-label"><p class="product-name">Steady-Stem Tree</p><p class="product-code">Product #TR2847</p></div></article>
        <article class="product"><div class="product-photo tone-poinsettia" role="img" aria-label="Red poinsettia arrangement"></div><div class="product-label"><p class="product-name">Red Poinsettia</p><p class="product-code">Product #LG2031</p></div></article>
        <article class="product"><div class="product-photo tone-amaryllis" role="img" aria-label="Red amaryllis and white rose arrangement"></div><div class="product-label"><p class="product-name">Red Amaryllis Mix</p><p class="product-code">Product #LG2278</p></div></article>
        <article class="product"><div class="product-photo tone-mum" role="img" aria-label="White mum, yellow rose and light blue hydrangea arrangement"></div><div class="product-label"><p class="product-name">White Mum and Light Blue Hydrangea Mix</p><p class="product-code">Product #LG2153</p></div></article>
        <article class="product"><div class="product-photo tone-blue" role="img" aria-label="Blue rose and lily arrangement"></div><div class="product-label"><p class="product-name">Blue Rose and Lily Mix</p><p class="product-code">Product #LG2127</p></div></article>
        <article class="product"><div class="product-photo tone-poppy" role="img" aria-label="Red and orange poppy arrangement"></div><div class="product-label"><p class="product-name">Red &amp; Orange Poppy Mix</p><p class="product-code">Product #LG2311</p></div></article>
        <article class="product"><div class="product-photo tone-burgundy" role="img" aria-label="Burgundy rose and lily arrangement"></div><div class="product-label"><p class="product-name">Burgundy Rose and Lily Mix</p><p class="product-code">Product #LG2015</p></div></article>
        <article class="product"><div class="product-photo tone-pink" role="img" aria-label="Pink rose and hydrangea arrangement"></div><div class="product-label"><p class="product-name">Pink Rose and Hygrangea Mix</p><p class="product-code">Product #LG2480</p></div></article>
        <article class="product"><div class="product-photo tone-yellow" role="img" aria-label="Yellow rose and hydrangea arrangement"></div><div class="product-label"><p class="product-name">Yellow Rose and Hydrangea Mix</p><p class="product-code">Product #LG2481</p></div></article>
      </div>
    </section>

    <section class="page page--right">
      <div class="page-rule"></div>
      <div class="flourish flourish--left" role="img" aria-label="Silver ornamental flourish"></div>
      <div class="flourish flourish--right" role="img" aria-label="Silver ornamental flourish"></div>
      <h2 class="section-title">Seasons (Christmas)</h2>
      <div class="product-grid">
        <article class="product"><div class="product-photo tone-tree" role="img" aria-label="Decorated Christmas tree arrangement with red bow"></div><div class="product-label"><p class="product-name">Steady-Stem Tree</p><p class="product-code">Product #TR2847</p></div></article>
        <article class="product"><div class="product-photo tone-poinsettia" role="img" aria-label="Red poinsettia arrangement"></div><div class="product-label"><p class="product-name">Red Poinsettia</p><p class="product-code">Product #LG2031</p></div></article>
        <article class="product"><div class="product-photo tone-amaryllis" role="img" aria-label="Red amaryllis and white rose arrangement"></div><div class="product-label"><p class="product-name">Red Amaryllis Mix</p><p class="product-code">Product #LG2278</p></div></article>
        <article class="product"><div class="product-photo tone-mum" role="img" aria-label="White mum, yellow rose and light blue hydrangea arrangement"></div><div class="product-label"><p class="product-name">White Mum and Light Blue Hydrangea Mix</p><p class="product-code">Product #LG2153</p></div></article>
        <article class="product"><div class="product-photo tone-blue" role="img" aria-label="Blue rose and lily arrangement"></div><div class="product-label"><p class="product-name">Blue Rose and Lily Mix</p><p class="product-code">Product #LG2127</p></div></article>
        <article class="product"><div class="product-photo tone-poppy" role="img" aria-label="Red and orange poppy arrangement"></div><div class="product-label"><p class="product-name">Red &amp; Orange Poppy Mix</p><p class="product-code">Product #LG2311</p></div></article>
        <article class="product"><div class="product-photo tone-burgundy" role="img" aria-label="Burgundy rose and lily arrangement"></div><div class="product-label"><p class="product-name">Burgundy Rose and Lily Mix</p><p class="product-code">Product #LG2015</p></div></article>
        <article class="product"><div class="product-photo tone-pink" role="img" aria-label="Pink rose and hydrangea arrangement"></div><div class="product-label"><p class="product-name">Pink Rose and Hygrangea Mix</p><p class="product-code">Product #LG2480</p></div></article>
        <article class="product"><div class="product-photo tone-yellow" role="img" aria-label="Yellow rose and hydrangea arrangement"></div><div class="product-label"><p class="product-name">Yellow Rose and Hydrangea Mix</p><p class="product-code">Product #LG2481</p></div></article>
      </div>
    </section>

    <div class="edge-band">
      <span class="band-grey" style="width:192px"></span>
      <span class="band-red" style="width:193px"></span>
      <span class="band-gold" style="width:373px"></span>
      <span class="band-red" style="width:192px"></span>
      <span class="band-grey" style="width:190px"></span>
    </div>
  </main>

  <div class="trim trim--h" style="top:163px"></div>
  <div class="trim trim--h" style="top:885px"></div>
  <div class="trim trim--v" style="left:38px"></div>
  <div class="trim trim--v" style="left:600px"></div>
  <div class="trim trim--v" style="left:1162px"></div>
</body>
</html>
```